Jotle - sticky notes for DeskOS landing page single page html + css

Is landing page for a new DeskOS app, I need just one single page explaing some features.

I will attach some materials to get insiprations.

Should be used the latest model of devices and some nice features
you can try the app here http://qv.example/f/K8R2

Jotle is a simple note taking app for DeskOS

Features:
- SkyVault Sync on differnt Deskbook
- Private notes
- PressKey Support on Deskbook to quick unlock
- Custom Colors
- Rich Text editing
- Glide Strip support
- Autolock private notes after user activity

some text should be present as spot
Updates

We have a new icon: http://qv.example/i/pm47

Project Deadline Extended
Reason: Delayed to have more time to develope ideas

Target Market(s)

US

Industry/Entity Type

Software

Coding

Coded - Design and coding required

Number of Pages Required

1 page

Font styles to use
Sans Serif

Colors
fbed22

Requirements
Must have
• Fast load and adaptable to verious devices
• some menu that point down to the features sections
• - link to Desk App Depot with badge
• - Form to subscribe a newsletter
• - Use some claim text
• - Avenir font
• some screenshot of the prduct
Nice to have
• some animations but not to much
• references:
• http://quillhourapp.example
• https://marovinapp.example
• http://www.hueforge.example/mac/
• https://crankworks.example/clipmule/
• https://crankworks.example/chirpling/mac/
• http://www.otter-scribe.example
Should not have
• slow load

```html
<!DOCTYPE html>
<html lang="en">
<head>
<meta charset="utf-8">
<title>Jotle – sticky notes for DeskOS</title>
<link rel="stylesheet" href="https://fonts.googleapis.com/css2?family=Open+Sans:wght@300;400;600;700&display=swap">
<style>
:root{
  --yellow:#f9bd0b;
  --yellow-light:#fbe122;
  --ink:#222222;
  --text:#555555;
  --muted:#8a8a8a;
  --line:#d6d6d6;
  --band:#f2f2f2;
  --white:#ffffff;
  --footer:#2d2d2d;
  --blue:#2a9fd8;
  --red:#e63a2e;
  --brown:#8a5a2b;
  --green:#29a35a;
}
*{box-sizing:border-box;margin:0;padding:0}
html,body{width:1200px;height:3390px;overflow:hidden}
body{font-family:"Open Sans",Arial,sans-serif;color:var(--ink);background:var(--white);position:relative}
section,header,footer{position:absolute;left:0;width:1200px}
.abs{position:absolute}
p{font-size:14px;line-height:21px;color:var(--text)}

/* nav */
.site-nav{top:0;height:77px;background:var(--white)}
.brand{left:100px;top:18px;display:flex;align-items:center;gap:10px}
.brand-dot{width:34px;height:34px;border-radius:50%;background:var(--yellow-light)}
.brand-name{font-size:24px;font-weight:600;color:var(--ink)}
.menu{right:95px;top:16px;display:flex;align-items:center}
.menu a{font-size:14px;font-weight:600;color:var(--ink);text-decoration:none;margin-left:30px}
.menu a.current{color:var(--muted);font-weight:400}
.menu a.btn-download{background:var(--yellow);color:var(--white);padding:12px 22px;border-radius:24px;margin-left:22px}

/* hero */
.hero{top:77px;height:470px;background:var(--band)}
.hero-title{left:100px;top:128px;font-size:52px;font-weight:300;line-height:66px;color:var(--ink);letter-spacing:1px}
.btn-outline{left:100px;top:300px;width:150px;height:46px;border:2px solid var(--yellow-light);border-radius:24px;font-size:20px;font-weight:600;color:var(--ink);display:flex;align-items:center;justify-content:center}
.hero-devices{left:600px;top:86px;width:540px;height:290px;border-radius:8px;background:linear-gradient(135deg,#3a3a3a 0%,#fbe122 35%,#ffd400 70%,#cfcfcf 100%)}
.dots{display:flex;gap:16px}
.dots span{width:12px;height:12px;border-radius:50%;background:#c8c8c8}
.dots span.on{background:#555}
.hero .dots{left:566px;top:429px}

/* app intro */
.app-intro{top:547px;height:429px;background:var(--white)}
.app-title{left:100px;top:40px;width:475px;text-align:center;font-size:28px;font-weight:400}
.app-copy{left:100px;top:97px;width:475px}
.app-phones{left:192px;top:176px;width:408px;height:206px;border-radius:10px 10px 0 0;background:linear-gradient(120deg,#2b2b2b 0%,#fbe122 40%,#ffd400 75%,#e8e8e8 100%)}
.perk{width:236px;height:152px;border:1px solid var(--line);display:flex;flex-direction:column;align-items:center;justify-content:center;gap:14px;font-size:15px;color:var(--ink)}
.perk.active{border:3px solid var(--yellow-light)}

/* pricing */
.pricing{top:976px;height:475px;background:var(--band)}
.pricing-title{left:100px;top:18px;font-size:28px;font-weight:400}
.pricing-sub{left:100px;top:68px;font-size:15px;color:var(--text)}
.accent-rule{left:100px;top:117px;width:46px;height:3px;background:var(--yellow)}
.pricing-copy1{left:100px;top:148px;width:640px;font-size:13px;line-height:20px}
.pricing-copy2{left:100px;top:243px;width:640px;font-size:13px;line-height:20px}
.tier-tabs{left:102px;top:342px;display:flex;gap:10px}
.tier{width:110px;height:112px;border:1px solid #cfcfcf;display:flex;flex-direction:column;align-items:center;justify-content:center;gap:18px;font-size:14px;color:var(--muted)}
.tier.active{border-bottom:4px solid var(--yellow)}
.plan{left:798px;top:21px;width:303px;height:436px;background:var(--white);border:2px solid #9a9a9a}
.plan-head{height:75px;border-bottom:1px solid var(--line);display:flex;align-items:center;justify-content:center;font-size:22px;letter-spacing:1px}
.plan-list{list-style:none;text-align:center;padding-top:12px;height:218px;border-bottom:1px solid var(--line)}
.plan-list li{font-size:12px;color:var(--muted);line-height:39px}
.price{text-align:center;margin-top:14px;font-size:46px;line-height:50px;font-weight:600}
.price sup{font-size:16px;vertical-align:18px}
.price sub{font-size:12px;font-weight:400;vertical-align:-2px}
.btn-solid{background:var(--yellow);color:var(--white);border-radius:24px;display:flex;align-items:center;justify-content:center;font-size:13px;font-weight:600}
.plan .btn-solid{margin:10px auto 0;width:146px;height:43px}

/* features */
.features{top:1451px;height:639px;background:var(--white)}
.sec-title{width:1200px;text-align:center;font-size:30px;font-weight:400}
.features .sec-title{top:40px}
.features-sub{left:340px;top:90px;width:520px;text-align:center}
.feature{width:300px}
.feature svg{display:block;margin-bottom:18px}
.feature h3{font-size:15px;font-weight:600;margin-bottom:12px}
.feature p{font-size:13px;line-height:20px}
.feature-last{left:440px;top:488px;width:360px;height:140px}
.feature-last h3{position:absolute;left:55px;top:10px;font-size:15px;font-weight:600}
.feature-last p{position:absolute;left:50px;top:52px;width:300px;text-align:center;font-size:13px;line-height:20px}

/* testimonials */
.testimonials{top:2090px;height:369px;background:var(--band)}
.testimonials .sec-title{top:22px}
.avatar{left:525px;top:85px;width:135px;height:135px;border-radius:50%;background:radial-gradient(circle at 50% 45%,#d9b59a 0%,#8a6a55 60%,#5a4a40 100%)}
.quote{left:180px;top:232px;width:840px;text-align:center;font-size:18px;line-height:30px;color:#888}
.quote-by{left:872px;top:280px;font-size:21px;color:var(--ink)}
.testimonials .dots{left:540px;top:324px}
.testimonials .dots span{background:#fbe122;opacity:.45}
.testimonials .dots span.on{opacity:1;background:var(--yellow)}

/* download */
.download{top:2459px;height:294px;background:var(--white)}
.download-title{left:100px;top:38px;width:520px;font-size:29px;font-weight:600;line-height:39px}
.download-copy{left:100px;top:125px;width:480px}
.download .btn-solid{left:100px;top:194px;width:146px;height:46px;font-size:15px;font-weight:400}
.store-badge{left:866px;top:88px;width:212px;height:104px;border-radius:14px;background:#1e1e1e}

/* contact */
.contact{top:2753px;height:434px;background:var(--white);border-top:2px solid #bdbdbd}
.contact .sec-title{top:12px}
.field{left:100px;width:428px;border:1px solid var(--line);font-size:14px;color:var(--ink);padding:12px 20px}
.contact .btn-solid{left:103px;top:362px;width:146px;height:44px;font-size:14px;font-weight:700}
.contact-copy{left:630px;top:64px;width:380px}
.contact-row{left:630px;display:flex;align-items:center;gap:12px;font-size:18px}
.contact-row strong{font-weight:600;width:95px}
.socials{left:632px;top:358px;display:flex;gap:14px}
.socials span{width:14px;height:14px;border-radius:50%;background:var(--ink)}

/* footer */
.site-footer{top:3187px;height:203px;background:var(--footer)}
.footer-brand{left:0;top:34px;width:1200px;display:flex;justify-content:center;align-items:center;gap:10px}
.footer-brand .brand-dot{width:28px;height:28px}
.footer-brand .brand-name{color:var(--yellow-light);font-size:22px}
.footer-links{left:0;top:106px;width:1200px;display:flex;justify-content:center;gap:32px}
.footer-links a{color:var(--white);text-decoration:none;font-size:14px}
.footer-links a.current{color:var(--yellow)}
.copyright{left:0;top:148px;width:1200px;text-align:center;color:var(--white);font-size:13px}
</style>
</head>
<body>

<header class="site-nav">
  <div class="abs brand"><span class="brand-dot"></span><span class="brand-name">Jotle</span></div>
  <nav class="abs menu">
    <a class="current" href="#home">Home</a>
    <a href="#about">About</a>
    <a href="#pricing">Pricing</a>
    <a href="#features">Features</a>
    <a href="#testimonial">Testimonial</a>
    <a href="#contact">Contact</a>
    <a class="btn-download" href="#download">Download Now</a>
  </nav>
</header>

<section class="hero" id="home">
  <h1 class="abs hero-title">KEEP YOUR NOTES<br>SAFE</h1>
  <div class="abs btn-outline">Get Now</div>
  <div class="abs hero-devices" role="img" aria-label="Jotle app shown on a laptop, tablet and phone with yellow screens"></div>
  <div class="abs dots"><span></span><span class="on"></span><span></span></div>
</section>

<section class="app-intro" id="about">
  <h2 class="abs app-title">JOTLE APP</h2>
  <p class="abs app-copy">Lorem ipsum dolor sit amet, consectetur adipisicing elit. Delectus dolor es numquam, maxime architecto optio a tenetur commodi</p>
  <div class="abs app-phones" role="img" aria-label="Two phones showing the Jotle app screen"></div>

  <div class="abs perk active" style="left:612px;top:51px">
    <svg width="40" height="34" viewBox="0 0 40 34"><path d="M4 30a16 16 0 1 1 32 0z" fill="#f9bd0b"/><circle cx="20" cy="28" r="3" fill="#fff"/><path d="M20 28 27 16" stroke="#fff" stroke-width="3"/><circle cx="10" cy="22" r="2" fill="#fff"/><circle cx="14" cy="13" r="2" fill="#fff"/><circle cx="26" cy="11" r="2" fill="#fff"/></svg>
    <span>Total Security</span>
  </div>
  <div class="abs perk" style="left:873px;top:51px">
    <svg width="24" height="40" viewBox="0 0 24 40"><path d="M14 2 3 22h8l-3 16 13-22h-8z" fill="#c9c9c9"/></svg>
    <span>Powerful System</span>
  </div>
  <div class="abs perk" style="left:612px;top:230px">
    <svg width="46" height="36" viewBox="0 0 46 36"><path d="M10 2h26l8 10-21 22L2 12z M2 12h42 M16 2l-4 10 11 22 11-22-4-10" fill="none" stroke="#c9c9c9" stroke-width="2"/></svg>
    <span>Clean Design</span>
  </div>
  <div class="abs perk" style="left:873px;top:230px">
    <svg width="40" height="36" viewBox="0 0 40 36"><g stroke="#c9c9c9" stroke-width="2"><path d="M2 6h36M2 18h36M2 30h36"/></g><g fill="#fff" stroke="#c9c9c9" stroke-width="2"><circle cx="26" cy="6" r="4"/><circle cx="12" cy="18" r="4"/><circle cx="22" cy="30" r="4"/></g></svg>
    <span>User Friendly</span>
  </div>
</section>

<section class="pricing" id="pricing">
  <h2 class="abs pricing-title">Pricing Stats</h2>
  <p class="abs pricing-sub">We Offer Special Pricing Offer For You</p>
  <div class="abs accent-rule"></div>
  <p class="abs pricing-copy1">Lorem ipsum dolor sit amet, consectetur adipisicing elit. Dicta cumque, consequuntur nesciunt repudiandae. Dolorum pariatur tempora nihil sunt! Dolorem quia incidunt qui cupiditate. Voluptatem doloremque quisquam error, neque nobis ipsa.</p>
  <p class="abs pricing-copy2">Lorem ipsum dolor sit amet, consectetur adipisicing elit. Dicta cumque, consequuntur nesciunt repudiandae. Dolorum pariatur tempora nihil sunt! Dolorem quia incidunt qui cupiditate. Voluptatem doloremque quisquam error, neque nobis ipsa.</p>
  <div class="abs tier-tabs">
    <div class="tier"><svg width="20" height="22" viewBox="0 0 20 22"><path d="M10 1 1 4v7c0 6 4 9 9 10 5-1 9-4 9-10V4z" fill="#777"/></svg>Basic</div>
    <div class="tier"><svg width="20" height="22" viewBox="0 0 20 22"><circle cx="10" cy="6" r="5" fill="#777"/><path d="M1 21c0-6 4-9 9-9s9 3 9 9z" fill="#777"/></svg>Personal</div>
    <div class="tier"><svg width="22" height="22" viewBox="0 0 22 22"><path d="M2 2h18v8c0 6-4 10-9 11C6 20 2 16 2 10z" fill="#777"/><path d="M7 9l4 4 4-4" stroke="#fff" stroke-width="2.5" fill="none"/></svg>Professional</div>
    <div class="tier active"><svg width="24" height="22" viewBox="0 0 24 22"><path d="M2 8h5l12-6v18L7 14H2z M8 14l2 7h3l-2-7" fill="#f9bd0b"/></svg>Business</div>
  </div>
  <div class="abs plan">
    <div class="plan-head">BASIC</div>
    <ul class="plan-list">
      <li>100gb storage</li><li>email setting</li><li>100 free email</li><li>built sms</li><li>notification</li>
    </ul>
    <div class="price"><sup>$</sup>99<sub>/m</sub></div>
    <div class="btn-solid">BUY App</div>
  </div>
</section>

<section class="features" id="features">
  <h2 class="abs sec-title">Jotle Features</h2>
  <p class="abs features-sub">Lorem ipsum dolor sit amet, consectetur adipisicing elit. Delectus dolor es numquam, maxime architecto optio a tenetur commodi</p>

  <div class="abs feature" style="left:100px;top:160px">
    <svg width="56" height="40" viewBox="0 0 56 40"><path d="M14 38a12 12 0 0 1-1-24A16 16 0 0 1 43 12a13 13 0 0 1-1 26z" fill="#2a9fd8"/><path d="M28 32V18m-7 6 7-7 7 7" stroke="#fff" stroke-width="3.5" fill="none"/></svg>
    <h3>SkyVault Sync on differnt Deskbook</h3>
    <p>Lorem ipsum dolor sit amet, consectetur adi pisi cing elit. Delectus dolores numquam, maxime architecto opti</p>
  </div>
  <div class="abs feature" style="left:445px;top:160px">
    <svg width="36" height="40" viewBox="0 0 36 40"><rect x="3" y="4" width="24" height="32" rx="2" fill="#e63a2e"/><path d="M8 14h14M8 20h14M8 26h9" stroke="#fff" stroke-width="2.5"/><path d="M26 8l6 6-12 14h-5v-5z" fill="#e63a2e" stroke="#fff" stroke-width="2"/></svg>
    <h3>Private notes</h3>
    <p>Lorem ipsum dolor sit amet, consectetur adi pisi cing elit. Delectus dolores numquam, maxime architecto opti</p>
  </div>
  <div class="abs feature" style="left:802px;top:160px">
    <svg width="36" height="40" viewBox="0 0 36 36"><path d="M18 18V2a16 16 0 0 1 16 16z" fill="#e63a2e"/><path d="M18 18h16a16 16 0 0 1-16 16z" fill="#2a9fd8"/><path d="M18 18v16A16 16 0 0 1 2 18z" fill="#29a35a"/><path d="M18 18H2A16 16 0 0 1 18 2z" fill="#f9bd0b"/></svg>
    <h3>Custom Colors</h3>
    <p>Lorem ipsum dolor sit amet, consectetur adi pisi cing elit. Delectus dolores numquam, maxime architecto opti</p>
  </div>

  <div class="abs feature" style="left:100px;top:335px">
    <svg width="40" height="36" viewBox="0 0 40 36"><path d="M2 6h34M2 18h34M2 30h34" stroke="#e63a2e" stroke-width="5"/></svg>
    <h3>Glide Strip support</h3>
    <p>Lorem ipsum dolor sit amet, consectetur adi pisi cing elit. Delectus dolores numquam, maxime architecto opti</p>
  </div>
  <div class="abs feature" style="left:445px;top:335px">
    <svg width="38" height="36" viewBox="0 0 38 36"><rect x="2" y="6" width="28" height="28" rx="2" fill="none" stroke="#8a5a2b" stroke-width="3"/><path d="M30 2l5 5-16 16-7 2 2-7z" fill="#8a5a2b"/></svg>
    <h3>Rich Text editing</h3>
    <p>Lorem ipsum dolor sit amet, consectetur adi pisi cing elit. Delectus dolores numquam, maxime architecto opti</p>
  </div>
  <div class="abs feature" style="left:802px;top:335px">
    <svg width="36" height="36" viewBox="0 0 36 36"><g fill="none" stroke="#29a35a" stroke-width="2.2"><path d="M7 10a14 14 0 0 1 22 0"/><path d="M5 20a13 13 0 0 1 26 0v4"/><path d="M10 32c0-6-1-8-1-12a9 9 0 0 1 18 0c0 4 0 8-2 12"/><path d="M14 33c0-6-1-9-1-13a5 5 0 0 1 10 0c0 5 0 9-2 13"/><path d="M18 20c0 5 0 9-1 14"/></g></svg>
    <h3>PressKey Support on Deskbook to quick unlock</h3>
    <p>Lorem ipsum dolor sit amet, consectetur adi pisi cing elit. Delectus dolores numquam, maxime architecto opti</p>
  </div>

  <div class="abs feature-last">
    <svg width="40" height="40" viewBox="0 0 40 40"><circle cx="20" cy="20" r="19" fill="#e63a2e"/><rect x="11" y="18" width="18" height="13" rx="2" fill="#fff"/><path d="M14 18v-4a6 6 0 0 1 12 0v4" fill="none" stroke="#fff" stroke-width="3"/><circle cx="20" cy="24" r="2" fill="#e63a2e"/></svg>
    <h3>Autolock private notes after user activity</h3>
    <p>Lorem ipsum dolor sit amet, consectetur adi pisi cing elit. Delectus dolores numquam, maxime architecto opti</p>
  </div>
</section>

<section class="testimonials" id="testimonial">
  <h2 class="abs sec-title">Testimonials</h2>
  <div class="abs avatar" role="img" aria-label="Round portrait photo of the reviewer"></div>
  <p class="abs quote">Lorem ipsum dolor sit amet, consectetur adipisicing elit. Delectus dolores numquam, maxime architecto optio a tenetur commodi neque deleniti aperiam.</p>
  <p class="abs quote-by">- Dario Lenkov</p>
  <div class="abs dots"><span class="on"></span><span></span><span></span></div>
</section>

<section class="download" id="download">
  <h2 class="abs download-title">Keep ypur jotle in a safe place in sync with your all device</h2>
  <p class="abs download-copy">Lorem ipsum dolor sit amet, consectetur adipisicing elit. Delectus dolor es numquam, maxime architecto optio a tenetur commodi</p>
  <div class="abs btn-solid">Learn More</div>
  <div class="abs store-badge" role="img" aria-label="Desk App Depot download badge"></div>
</section>

<section class="contact" id="contact">
  <h2 class="abs sec-title">Contact us</h2>
  <div class="abs field" style="top:67px;height:45px">Name</div>
  <div class="abs field" style="top:125px;height:45px">Your Email</div>
  <div class="abs field" style="top:185px;height:155px">Message</div>
  <div class="abs btn-solid">SEAND MESSAGE</div>
  <p class="abs contact-copy">Lorem ipsum dolor sit amet, consectetur adipisicing elit. Delectus dolores numquam, maxime architecto optio a tenetur commodi</p>
  <div class="abs contact-row" style="top:195px">
    <svg width="22" height="22" viewBox="0 0 22 22"><path d="M5 1l4 5-2 3c1 3 3 5 6 6l3-2 5 4-2 4C10 21 1 12 1 3z" fill="#222"/></svg>
    <strong>Call Now</strong><span>+2540175382</span>
  </div>
  <div class="abs contact-row" style="top:245px">
    <svg width="22" height="18" viewBox="0 0 22 18"><rect x="1" y="1" width="20" height="16" fill="#222"/><path d="M1 1l10 9 10-9" stroke="#fff" stroke-width="2" fill="none"/></svg>
    <strong>Mail Now</strong><span>hello@jotle.example</span>
  </div>
  <div class="abs contact-row" style="top:295px">
    <svg width="22" height="26" viewBox="0 0 22 26"><path d="M11 1a9 9 0 0 1 9 9c0 7-9 15-9 15S2 17 2 10a9 9 0 0 1 9-9z" fill="#222"/><circle cx="11" cy="10" r="3.5" fill="#fff"/></svg>
    <strong>Find Us</strong><span>lorem ipsm,dolor sit</span>
  </div>
  <div class="abs socials"><span></span><span></span><span></span><span></span><span></span><span></span></div>
</section>

<footer class="site-footer">
  <div class="abs footer-brand"><span class="brand-dot"></span><span class="brand-name">Jotle</span></div>
  <nav class="abs footer-links">
    <a class="current" href="#home">Home</a><a href="#about">About</a><a href="#pricing">Pricing</a><a href="#features">Features</a><a href="#gallery">Gallery</a><a href="#contact">Contact</a><a href="#download">Download Now</a>
  </nav>
  <p class="abs copyright">@2017 jotle app.all right reserved</p>
</footer>

</body>
</html>
```